Netvale - Seafood industry professional promoting page

Hi. I´m in the seafood business with a one man company sourcing and exporting frozen seafood. I need to make a one page homepage for Netvale (from Iceland). The feeling of it should be; Trustworthy, experience and knowledge.
Using as background a picture (or part of it), or a moving video:

http://www1.bryla.is/vefur/myndir/lysingur.jpg
https://clipvault.example/583027416

Main text to be:

- We can help source, market and add value to your seafood business
- Years of experience in seafood trade and production
- Extensive knowledge of fishing, seasonality, production and accreditations

Contact:
torvi@netvale.is
Tel: +3654172093
(with a photo)

p.s. please also make logo look better.

Target Market(s)

Seafood industry

Industry/Entity Type

Business

Logo Text

Netvale

Coding

Coded - Design and coding required

Number of Pages Required

1 page

Colors
0792cd
33a6d7

```html
<!DOCTYPE html>
<html lang="en">
<head>
<meta charset="utf-8">
<title>Netvale – Seafood sourcing and export</title>
<link rel="stylesheet" href="https://fonts.googleapis.com/css2?family=Open+Sans:wght@300;400;600;700&display=swap">
<style>
  :root {
    --brand-blue: #0792cd;
    --brand-blue-light: #33a6d7;
    --icon-blue: #1a86cf;
    --white: #ffffff;
    --frame: #e6e2da;
    --footer-bg: #232323;
    --footer-text: #b9b9b9;
    --bg-olive: #6f6d4e;
    --bg-grey: #5e5c55;
    --bg-dark: #2f2f30;
  }
  * { box-sizing: border-box; margin: 0; padding: 0; }
  html, body { width: 919px; height: 1200px; overflow: hidden; }
  body {
    position: relative;
    font-family: "Open Sans", sans-serif;
    color: var(--white);
    background: var(--bg-dark);
  }
  .page-backdrop {
    position: absolute; inset: 0 0 61px 0;
    background:
      radial-gradient(ellipse at 20% 20%, rgba(150,140,80,.55), transparent 55%),
      radial-gradient(ellipse at 85% 30%, rgba(130,125,90,.5), transparent 55%),
      linear-gradient(180deg, var(--bg-olive) 0%, var(--bg-grey) 45%, #4d4a40 70%, var(--bg-dark) 100%);
  }
  .brand-badge {
    position: absolute; left: 378px; top: 6px;
    width: 164px; height: 164px; border-radius: 50%;
    background: var(--white);
    display: flex; align-items: center; justify-content: center;
  }
  .brand-name {
    font-weight: 700; font-size: 27px; color: var(--brand-blue);
    letter-spacing: .5px;
  }
  .hero-frame {
    position: absolute; left: 76px; top: 178px;
    width: 767px; height: 329px;
    border: 9px solid var(--frame);
  }
  .hero-media {
    position: absolute; inset: 0;
    background:
      radial-gradient(ellipse at 75% 75%, rgba(215,215,220,.85), transparent 55%),
      linear-gradient(160deg, #1d4b74 0%, #2f6692 40%, #6e8ea8 70%, #b9c0c6 100%);
  }
  .hero-tagline {
    position: absolute; left: 0; right: 0; top: 112px;
    text-align: center; font-size: 21px; font-weight: 400;
  }
  .hero-play { position: absolute; left: 336px; top: 150px; }
  .experience-heading {
    position: absolute; left: 0; right: 0; top: 552px;
    text-align: center; font-size: 26px; font-weight: 700;
  }
  .strengths { position: absolute; top: 684px; left: 0; right: 0; }
  .strength {
    position: absolute; width: 240px; margin-left: -120px;
    text-align: center;
  }
  .strength-icon {
    width: 103px; height: 103px; margin: 0 auto;
    border-radius: 50%; background: var(--icon-blue);
    display: flex; align-items: center; justify-content: center;
  }
  .strength-label {
    margin-top: 17px; font-size: 11.5px; font-weight: 600;
    text-transform: uppercase;
  }
  .contact-heading {
    position: absolute; left: 0; right: 0; top: 916px;
    text-align: center; font-size: 34px; font-weight: 300;
  }
  .contact-photo {
    position: absolute; left: 288px; top: 982px;
    width: 116px; height: 116px; border-radius: 50%;
    background: radial-gradient(circle at 50% 45%, #cfcfcf, #8a8a8a 70%, #e8e8e8);
  }
  .contact-details {
    position: absolute; left: 426px; top: 1014px;
    font-size: 14px; font-weight: 300; line-height: 28px;
  }
  .contact-details svg { vertical-align: -2px; margin-right: 4px; }
  .site-footer {
    position: absolute; left: 0; right: 0; bottom: 0; height: 61px;
    background: var(--footer-bg); color: var(--footer-text);
    font-size: 11px; text-align: center; line-height: 61px;
  }
</style>
</head>
<body>
  <div class="page-backdrop" role="img" aria-label="Blurred coastal fishing photograph as page background"></div>

  <header class="brand-badge">
    <span class="brand-name">NETVALE</span>
  </header>

  <section class="hero-frame">
    <div class="hero-media" role="img" aria-label="Underwater video still of fish swimming overhead"></div>
    <p class="hero-tagline">We can help source, market and add value to your seafood business</p>
    <svg class="hero-play" width="78" height="78" viewBox="0 0 78 78" aria-label="Play video">
      <circle cx="39" cy="39" r="37" fill="none" stroke="rgba(255,255,255,.7)" stroke-width="3"/>
      <path d="M30 24 L55 39 L30 54 Z" fill="none" stroke="rgba(255,255,255,.75)" stroke-width="3" stroke-linejoin="round"/>
    </svg>
  </section>

  <h1 class="experience-heading">Years of experience in seafood trade and production</h1>

  <section class="strengths">
    <div class="strength" style="left:202px">
      <div class="strength-icon">
        <svg width="95" height="95" viewBox="0 0 95 95">
          <circle cx="47.5" cy="47.5" r="43" fill="none" stroke="#fff" stroke-width="2.5"/>
          <path d="M28 48 H64 L59 55 H32 Z" fill="#fff"/>
          <rect x="38" y="42" width="14" height="6" fill="#fff"/>
          <path d="M56 46 Q62 36 72 34" fill="none" stroke="#fff" stroke-width="1.5"/>
          <path d="M27 59 q5 -3 10 0 t10 0 t10 0 t10 0" fill="none" stroke="#fff" stroke-width="2"/>
          <path d="M27 64 q5 -3 10 0 t10 0 t10 0 t10 0" fill="none" stroke="#fff" stroke-width="2"/>
        </svg>
      </div>
      <p class="strength-label">Extensive knowledge of fishing</p>
    </div>
    <div class="strength" style="left:460px">
      <div class="strength-icon">
        <svg width="95" height="95" viewBox="0 0 95 95">
          <circle cx="47.5" cy="47.5" r="43" fill="none" stroke="#fff" stroke-width="2.5"/>
          <path d="M27 62 L45 40 L50 45 L53 42 L68 62 Z" fill="#fff"/>
          <line x1="51" y1="42" x2="51" y2="29" stroke="#fff" stroke-width="1.5"/>
          <path d="M51 29 H59 L57 32 L59 35 H51 Z" fill="#fff"/>
        </svg>
      </div>
      <p class="strength-label">Seasonality</p>
    </div>
    <div class="strength" style="left:717px">
      <div class="strength-icon">
        <svg width="95" height="95" viewBox="0 0 95 95">
          <circle cx="47.5" cy="47.5" r="43" fill="none" stroke="#fff" stroke-width="2.5"/>
          <circle cx="46" cy="33" r="5" fill="#fff"/>
          <circle cx="52" cy="30" r="5" fill="#fff"/>
          <rect x="34" y="38" width="8" height="26" fill="#fff"/>
          <path d="M34 64 V48 L48 42 V48 L62 42 V64 Z" fill="#fff"/>
          <rect x="40" y="54" width="5" height="5" fill="#1a86cf"/>
          <rect x="50" y="54" width="5" height="5" fill="#1a86cf"/>
        </svg>
      </div>
      <p class="strength-label">Production and accreditations</p>
    </div>
  </section>

  <h2 class="contact-heading">Contact Us</h2>
  <div class="contact-photo" role="img" aria-label="Portrait photo of the company owner"></div>
  <address class="contact-details" style="font-style:normal">
    <div>
      <svg width="14" height="11" viewBox="0 0 14 11"><rect x="0.75" y="0.75" width="12.5" height="9.5" fill="none" stroke="#fff" stroke-width="1.5"/><path d="M1 1 L7 6 L13 1" fill="none" stroke="#fff" stroke-width="1.5"/></svg>torvi@netvale.is
    </div>
    <div>
      <svg width="12" height="12" viewBox="0 0 24 24"><path fill="#fff" d="M6.6 10.8a15.1 15.1 0 0 0 6.6 6.6l2.2-2.2c.3-.3.7-.4 1-.2 1.1.4 2.3.6 3.6.6.6 0 1 .4 1 1V20c0 .6-.4 1-1 1A17 17 0 0 1 3 4c0-.6.4-1 1-1h3.5c.6 0 1 .4 1 1 0 1.3.2 2.5.6 3.6.1.3 0 .7-.2 1z"/></svg>Tel: +3654172093
    </div>
  </address>

  <footer class="site-footer">© 2018 Netvale.&nbsp; All right reserved . Term of Use</footer>
</body>
</html>
```